Venmoor Private Capital Ltd - corporate branding & website

We need a logo and stationery design for our private equity company called Venmoor Private Capital Limited. Our corporate colours are orange and grey. We would like something funky and modern and have elements that we can use easily on our proposed website and power point presentations so all our corporate communications are consistent in look & feel.

Target Market(s)

Property and financial investments

Industry/Entity Type

Equity

Contact Information for Business Card

Lewis Pembury
Director

Logo Text

Venmoor Private Capital

Number of Pages Required

3 page

Font styles to use
Serif

Colors
f37122
34a7d8
757575

Requirements
Must have
• A funky and interesting design, something creative but not totally out there.
• A consistent look and feel throughout our branded communications

```html
<!DOCTYPE html>
<html lang="en">
<head>
<meta charset="utf-8">
<title>Venmoor Private Capital – Stationery</title>
<link href="https://fonts.googleapis.com/css2?family=Montserrat:wght@400;500;600&display=swap" rel="stylesheet">
<style>
  :root {
    --orange: #d9961b;
    --orange-deep: #c9850f;
    --grey: #5b5b5b;
    --grey-light: #9a9a9a;
    --paper: #ffffff;
    --backdrop: #ececec;
    --text: #4a4a4a;
  }
  * { box-sizing: border-box; margin: 0; padding: 0; }
  html, body { width: 1200px; height: 795px; overflow: hidden; }
  body {
    background: var(--backdrop);
    font-family: "Montserrat", Arial, sans-serif;
    color: var(--text);
    position: relative;
  }
  .sheet {
    position: absolute;
    background: var(--paper);
    box-shadow: 0 2px 6px rgba(0,0,0,.12);
    overflow: hidden;
  }

  /* Brand name lockup */
  .brand { display: flex; align-items: center; gap: 6px; }
  .brand-mark { width: 9px; height: 9px; background: var(--orange); flex: none; }
  .brand-name { font-weight: 500; color: var(--grey); white-space: nowrap; letter-spacing: .2px; }
  .brand--light .brand-mark { background: var(--paper); }
  .brand--light .brand-name { color: var(--paper); }

  /* Contact block */
  .contact { list-style: none; }
  .contact li { display: flex; align-items: center; gap: 4px; font-size: 5px; line-height: 8px; color: var(--text); }
  .contact li::before { content: ""; width: 4px; height: 4px; border-radius: 50%; background: var(--grey); flex: none; }
  .contact-bar { height: 4px; background: var(--orange); }

  /* Letterhead */
  .letterhead { left: 60px; top: 157px; width: 340px; height: 481px; }
  .letterhead .brand { position: absolute; left: 34px; top: 32px; }
  .letterhead .brand-name { font-size: 11px; }
  .letter-body { position: absolute; left: 34px; top: 78px; width: 250px; }
  .letter-greeting { font-size: 7px; margin-bottom: 10px; }
  .letter-body p { font-size: 4.6px; line-height: 7px; margin-bottom: 7px; color: #555; text-align: justify; }
  .letterhead .contact { position: absolute; left: 34px; bottom: 46px; }
  .letterhead .contact-bar { position: absolute; left: 34px; bottom: 38px; width: 52px; }
  .letterhead .corner-band { position: absolute; right: 0; bottom: 0; width: 86px; height: 58px; background: var(--orange); }
  .letterhead .corner-band::after { content: ""; position: absolute; left: 28px; top: 0; width: 22px; height: 58px; background: var(--grey); }

  /* Folder */
  .folder { left: 430px; top: 157px; width: 340px; height: 481px; background: var(--orange); }
  .folder-pattern { position: absolute; inset: 0; background: linear-gradient(135deg, var(--orange) 0%, var(--orange-deep) 100%); }
  .folder .brand { position: absolute; left: 50%; top: 50%; transform: translate(-50%, -50%); gap: 8px; }
  .folder .brand-mark { width: 12px; height: 12px; }
  .folder .brand-name { font-size: 16px; }

  /* Envelopes */
  .envelope { left: 800px; width: 340px; height: 170px; }
  .envelope--front { top: 157px; }
  .envelope--front .brand { position: absolute; left: 22px; top: 20px; }
  .envelope--front .brand-name { font-size: 9px; }
  .envelope--front .contact { position: absolute; left: 22px; top: 70px; }
  .envelope--front .contact-bar { position: absolute; left: 22px; top: 108px; width: 48px; }
  .envelope--front .corner-band { position: absolute; right: 0; bottom: 0; width: 70px; height: 46px; background: var(--orange); }
  .envelope--front .corner-band::after { content: ""; position: absolute; left: 24px; top: 0; width: 18px; height: 46px; background: var(--grey); }
  .envelope--back { top: 345px; }
  .envelope-flap { position: absolute; left: 0; top: 0; width: 100%; height: 62px; background: var(--orange); }
  .envelope--back .brand { position: absolute; left: 26px; top: 100px; }
  .envelope--back .brand-name { font-size: 10px; }

  /* Business cards */
  .card { top: 533px; width: 160px; height: 91px; }
  .card--front { left: 800px; background: var(--orange); }
  .card--front .brand { position: absolute; left: 50%; top: 50%; transform: translate(-50%, -50%); }
  .card--front .brand-name { font-size: 8px; }
  .card--front .brand-mark { width: 7px; height: 7px; }
  .card--back { left: 980px; }
  .card--back .brand { position: absolute; left: 12px; top: 14px; gap: 4px; }
  .card--back .brand-mark { width: 6px; height: 6px; }
  .card--back .brand-name { font-size: 6px; }
  .card-person { position: absolute; left: 12px; top: 40px; }
  .card-person .name { font-size: 6px; font-weight: 600; color: var(--grey); }
  .card-person .role { font-size: 4.5px; color: var(--orange); }
  .card--back .contact { position: absolute; left: 80px; top: 36px; }
  .card--back .contact li { font-size: 4.2px; line-height: 7px; }
</style>
</head>
<body>

  <!-- Letterhead -->
  <section class="sheet letterhead">
    <div class="brand"><span class="brand-mark"></span><span class="brand-name">Venmoor Private Capital</span></div>
    <div class="letter-body">
      <p class="letter-greeting">Lorem ipsum dolor sit amet,</p>
      <p>Lorem ipsum dolor sit amet, consectetur adipiscing elit. Fusce ac sem in lectus mollis egestas. Sed non turpis nec justo gravida porta. Vestibulum ante ipsum primis in faucibus orci luctus et ultrices posuere cubilia curae. Integer tincidunt nibh at libero feugiat, sed aliquam urna volutpat. Donec varius felis vitae nisl sodales, eget rhoncus erat vulputate.</p>
      <p>Duis bibendum enim sollicitudin sem molestie pellentesque. Nunc suscipit lorem id turpis venenatis vehicula. Cras a magna non sapien luctus porttitor. Phasellus sit amet dolor vel orci tempor convallis. Nam pharetra ipsum quis metus fermentum, non aliquet augue faucibus. Aenean porttitor ex at lectus elementum, id mattis nisi tincidunt.</p>
      <p>Cras eu ligula pharetra, finibus nisl vel, mollis massa. Suspendisse potenti. Curabitur hendrerit tellus quis erat iaculis dignissim. Morbi tempus lectus sed ligula dictum, in volutpat neque ultrices. Quisque gravida nulla ac velit ullamcorper fringilla et eget dui.</p>
    </div>
    <ul class="contact">
      <li>+44 20 7946 0312</li>
      <li>info@venmoorcapital.co.uk</li>
      <li>18 Harlow Street, London</li>
      <li>www.venmoorcapital.co.uk</li>
    </ul>
    <div class="contact-bar"></div>
    <div class="corner-band"></div>
  </section>

  <!-- Folder -->
  <section class="sheet folder">
    <div class="folder-pattern" role="img" aria-label="Subtle tonal orange pattern covering the folder cover"></div>
    <div class="brand brand--light"><span class="brand-mark"></span><span class="brand-name">Venmoor Private Capital</span></div>
  </section>

  <!-- Envelope, front -->
  <section class="sheet envelope envelope--front">
    <div class="brand"><span class="brand-mark"></span><span class="brand-name">Venmoor Private Capital</span></div>
    <ul class="contact">
      <li>+44 20 7946 0312</li>
      <li>info@venmoorcapital.co.uk</li>
      <li>18 Harlow Street, London</li>
      <li>www.venmoorcapital.co.uk</li>
    </ul>
    <div class="contact-bar"></div>
    <div class="corner-band"></div>
  </section>

  <!-- Envelope, back -->
  <section class="sheet envelope envelope--back">
    <div class="envelope-flap"></div>
    <div class="brand"><span class="brand-mark"></span><span class="brand-name">Venmoor Private Capital</span></div>
  </section>

  <!-- Business card, front -->
  <section class="sheet card card--front">
    <div class="brand brand--light"><span class="brand-mark"></span><span class="brand-name">Venmoor Private Capital</span></div>
  </section>

  <!-- Business card, back -->
  <section class="sheet card card--back">
    <div class="brand"><span class="brand-mark"></span><span class="brand-name">Venmoor Private Capital</span></div>
    <div class="card-person">
      <p class="name">Lewis Pembury</p>
      <p class="role">Director</p>
    </div>
    <ul class="contact">
      <li>+44 20 7946 0312</li>
      <li>info@venmoorcapital.co.uk</li>
      <li>18 Harlow Street, London</li>
      <li>www.venmoorcapital.co.uk</li>
    </ul>
  </section>

</body>
</html>
```